Website for UK Fintech Company specialising in Auto-Finance asset management

We need a website for a FINTECH business called KELP Asset Management. We have developed and licenced an innovative platform to provide financial institutions whom provide secured Asset finance loans to consumer and commercial clients, allowing for real time tracking and management of defaulted accounts pending repossession. The KELP Asset Management platform is a total recoveries solution through the cycle, from the moment the lender has to recover the vehicle (due to default/non-payment) to the disposal of the vehicle (via sale at Motor Auctions or by selling to a Car dealership network). The data provided from external services allows the Financier to make informed decisions, such as whether it is economical to continue the recovery and decide which sales channel is better suited for their assets to maximise residual values and minimise financial losses. The KELP platform provides an array of MI reporting and uses a systematic approach utilising exception reporting to identify key areas of non-performance to enable focus where needed. KELP also provides a leading Debt collection service recovering end-of-cycle losses such as Financial Shortfall and losses in vehicle values due to conditions and excessive damage.

We also require a new logo for out new product called MB-Prismo

Target Market(s)

Financial institutions whom provide secured Asset finance loans to consumer and commercial clients

Industry/Entity Type

Financial Service

Logo Text

MB- Prismo (this is for a new product which forms part of the KELP Asset Mangement Platform

Number of Pages Required

4 page

Font styles to use
Serif
Sans Serif

Colors

Designer to choose colors to be used in the design.

Requirements
Must have
• We need a simple website with a broken down as follows;
• • Landing page
• • Services page
• • About us page
• • KELP Asset Management Platform login page (client facing)
Nice to have
• Our slogan is 'Auto-Finance Expertise'
• We are very much open to suggestions as long as we can create a professional/ corporate / modern feel to the website. We are a FINTECH company, and that needs to come across
Should not have
• Whilst we are an asset management company primarily managing vehicles through our platform, we don't want it to look like a car dealership website!:)

```html
<!DOCTYPE html>
<html lang="en">
<head>
<meta charset="utf-8">
<title>MB- Prismo</title>
<link href="https://fonts.googleapis.com/css2?family=Roboto:wght@300;400;500;700&display=swap" rel="stylesheet">
<style>
:root{
  --orange:#f07f06;
  --orange-dark:#c9680a;
  --ink:#3d3d3d;
  --heading:#4a4a4a;
  --muted:#6b6b6b;
  --rule:#e2e2e2;
  --footer-bar:#6e6e6e;
  --field-line:#d8d8d8;
}
*{box-sizing:border-box;margin:0;padding:0}
html,body{width:1200px;height:2550px;overflow:hidden;background:#fff}
body{font-family:'Roboto',sans-serif;color:var(--ink);position:relative}
.abs{position:absolute}
.btn{position:absolute;background:var(--orange);color:#fff;font-weight:500;font-size:14px;letter-spacing:.5px;
  display:flex;align-items:center;justify-content:center;border-bottom:3px solid var(--orange-dark);text-transform:uppercase}

/* header */
.site-header{position:absolute;left:0;top:0;width:1200px;height:85px;background:#fff;border-bottom:1px solid #f4c48f;z-index:2}
.brand{position:absolute;left:87px;top:22px;display:flex;align-items:center;gap:10px}
.brand-mark{width:32px;height:32px;background:var(--orange)}
.brand-name{font-size:26px;font-weight:700;color:var(--orange)}
.nav{position:absolute;top:37px;font-size:13.5px;letter-spacing:1px;color:#444}
.nav.active{color:var(--orange);border-bottom:2px solid var(--orange);padding-bottom:6px}
.login{position:absolute;left:1000px;top:30px;width:113px;height:26px;background:var(--orange);border-bottom:3px solid var(--orange-dark);
  color:#fff;font-size:11px;display:flex;align-items:center;justify-content:center;padding-left:18px}
.login-avatar{position:absolute;left:998px;top:26px;width:34px;height:34px;border-radius:50%;background:#fff;border:2px solid var(--orange)}

/* hero */
.hero{position:absolute;left:0;top:85px;width:1200px;height:488px;background:linear-gradient(135deg,#e9ece8 0%,#f4f4f2 45%,#e4e7e3 100%);border-bottom:3px solid #d6d6d6}
.hero-title{position:absolute;left:0;width:1200px;text-align:center;font-size:31px;font-weight:500;letter-spacing:1.5px;line-height:43px;color:#2b2b2b}

/* about */
.section-title{position:absolute;font-size:31px;font-weight:400;color:var(--heading);letter-spacing:1px}
.about-copy{position:absolute;left:87px;top:686px;width:498px;font-size:13.5px;line-height:21px;letter-spacing:.35px;color:#222}
.about-copy p+p{margin-top:21px}
.photo{position:absolute;box-shadow:0 2px 6px rgba(0,0,0,.35)}

/* services */
.services{position:absolute;left:0;top:1088px;width:1200px;height:622px;background:linear-gradient(160deg,#ececec 0%,#f3f3f1 50%,#e8e9e6 100%);border-bottom:2px solid #dcdcdc}
.service{position:absolute;width:270px;text-align:center}
.service-icon{width:105px;height:88px;margin:0 auto;background:var(--orange);border-bottom:3px solid var(--orange-dark);display:flex;align-items:center;justify-content:center}
.service-name{font-size:18px;color:#333;margin-top:14px}
.service-text{font-size:12.5px;line-height:19px;color:#222;margin-top:6px}

/* testimonial */
.arrow{position:absolute;width:41px;height:51px;display:flex;align-items:center;justify-content:center}
.arrow.prev{background:var(--orange)}
.arrow.next{background:#eeeeee;border:1px solid #ddd}
.quote-text{position:absolute;left:377px;top:1871px;width:615px;font-size:13.5px;line-height:21.5px;color:#666}
.quote-by{position:absolute;left:377px;top:1967px;font-size:13px;color:#555}
.quote-by .rule{display:inline-block;width:60px;height:1px;background:#ccc;vertical-align:middle;margin-right:22px}
.quote-by .name{color:#333;margin-right:14px}

/* footer */
.contact-zone{position:absolute;left:0;top:2048px;width:1200px;height:465px;background:linear-gradient(180deg,#f6f6f6,#fbfbfb);border-top:2px solid #e0e0e0}
.addr{position:absolute;left:110px;font-size:12.5px;line-height:21px;color:#666}
.addr-icon{position:absolute;left:87px}
.field{position:absolute;left:551px;width:562px;background:#fff;border:1px solid var(--field-line);box-shadow:0 2px 3px rgba(0,0,0,.12);
  font-size:12.5px;color:#888;padding:12px 10px}
.social{position:absolute;top:2422px;width:38px;height:38px;border-radius:50%;border:2px solid var(--orange)}
.footer-bar{position:absolute;left:0;top:2513px;width:1200px;height:37px;background:var(--footer-bar);color:#fff;font-size:13px;
  display:flex;align-items:center;justify-content:center}
</style>
</head>
<body>

<header class="site-header">
  <div class="brand"><span class="brand-mark"></span><span class="brand-name">MB Prismo</span></div>
  <span class="nav active" style="left:411px">HOME</span>
  <span class="nav" style="left:534px">ABOUT US</span>
  <span class="nav" style="left:686px">SERVICE</span>
  <span class="nav" style="left:826px">CONTACT US</span>
  <span class="login">Login</span>
  <span class="login-avatar"></span>
</header>

<section class="hero" role="img" aria-label="Faded background of banknotes and finance paperwork"></section>
<h1 class="hero-title" style="top:252px">LOREM IPSUM IS SIMPLY DUMMY TEXT OF THE<br>PRINTING AND TYPESHAS BEEN THE.</h1>
<span class="btn" style="left:503px;top:359px;width:194px;height:36px">Read More</span>

<h2 class="section-title" style="left:87px;top:626px">ABOUT US</h2>
<div class="about-copy">
  <p>Lorem Ipsum is simply dummy text of the printing and typesetting industry. Lorem Ipsum has been the industry's standard dummy text ever since the 1500s, when an unknown printer took a galley of type and scrambled it to make a type specimen book. Lorem Ipsum is simply dummy text of the printing and typesetting industry. Lorem Ipsum has been the industry's standard dummy text ever since the 1500s, when an unknown printer took a galley of type and scrambled it to make a type specimen book.</p>
  <p>Lorem Ipsum is simply dummy text of the printing and typesetting industry. Lorem Ipsum has been the industry's standard dummy text ever since the 1500s, when an unknown printer took a galley of type and scrambled it to make a type specimen book. Lorem Ipsum is simply dummy text of the printing and typesetting industry. Lorem Ipsum has been.</p>
</div>
<span class="btn" style="left:87px;top:991px;width:194px;height:36px">View More</span>
<div class="photo" style="left:816px;top:692px;width:297px;height:255px;background:linear-gradient(135deg,#4a4f5c,#8c8a78 55%,#3a3c42)" role="img" aria-label="Photo of banknotes being handed over"></div>
<div class="photo" style="left:617px;top:770px;width:240px;height:236px;border:3px solid #fff;background:linear-gradient(160deg,#e8ecef,#b9c2cb 55%,#f2f2f2)" role="img" aria-label="Photo of a business meeting at a desk"></div>

<section class="services" role="img" aria-label="Faded background of coins and banknotes"></section>
<h2 class="section-title" style="left:0;width:1200px;text-align:center;top:1141px">OUR SERVICES</h2>

<!-- Row 1: reporting, tracking, documents, recoveries -->
<div class="service" style="left:60px;top:1209px">
  <div class="service-icon"><svg width="48" height="44" viewBox="0 0 48 44" fill="#fff"><rect x="4" y="26" width="8" height="14"/><rect x="16" y="16" width="8" height="24"/><rect x="28" y="21" width="8" height="19"/><rect x="40" y="6" width="6" height="34"/><path d="M2 42h46" stroke="#fff" stroke-width="2"/></svg></div>
  <div class="service-name">LOREM IPSUM</div>
  <div class="service-text">Lorem ipsum dolor sit amet, consectetur adipiscing elit, sed do eiusmod tempor.</div>
</div>
<div class="service" style="left:324px;top:1209px">
  <div class="service-icon"><svg width="36" height="48" viewBox="0 0 36 48"><path d="M18 46C8 32 3 24 3 16a15 15 0 0 1 30 0c0 8-5 16-15 30z" fill="#fff"/><circle cx="18" cy="16" r="6" fill="#f07f06"/></svg></div>
  <div class="service-name">LOREM IPSUM</div>
  <div class="service-text">Lorem ipsum dolor sit amet, consectetur adipiscing elit, sed do eiusmod tempor.</div>
</div>
<div class="service" style="left:587px;top:1209px">
  <div class="service-icon"><svg width="44" height="50" viewBox="0 0 44 50" fill="none" stroke="#fff" stroke-width="2.5"><rect x="8" y="3" width="30" height="42"/><rect x="3" y="8" width="30" height="40" fill="#f07f06"/><path d="M10 20h16M10 28h16M10 35h16M10 41h10"/></svg></div>
  <div class="service-name">LOREM IPSUM</div>
  <div class="service-text">Lorem ipsum dolor sit amet, consectetur adipiscing elit, sed do eiusmod tempor.</div>
</div>
<div class="service" style="left:851px;top:1209px">
  <div class="service-icon"><svg width="48" height="48" viewBox="0 0 48 48" fill="none" stroke="#fff" stroke-width="3"><circle cx="24" cy="24" r="20"/><path d="M29 15a6 6 0 0 0-11 3v15h13M15 26h11M18 33h-3"/></svg></div>
  <div class="service-name">LOREM IPSUM</div>
  <div class="service-text">Lorem ipsum dolor sit amet, consectetur adipiscing elit, sed do eiusmod tempor.</div>
</div>

<!-- Row 2: security, performance, valuation, checklist -->
<div class="service" style="left:60px;top:1411px">
  <div class="service-icon"><svg width="42" height="48" viewBox="0 0 42 48" fill="none" stroke="#fff" stroke-width="3"><path d="M21 3 4 9v13c0 11 7 19 17 23 10-4 17-12 17-23V9z"/><path d="M13 24l6 6 10-11"/></svg></div>
  <div class="service-name">LOREM IPSUM</div>
  <div class="service-text">Lorem ipsum dolor sit amet, consectetur adipiscing elit, sed do eiusmod tempor.</div>
</div>
<div class="service" style="left:324px;top:1411px">
  <div class="service-icon"><svg width="52" height="38" viewBox="0 0 52 38" fill="none" stroke="#fff" stroke-width="3"><path d="M4 34a22 22 0 0 1 44 0"/><path d="M26 34 36 17"/><circle cx="26" cy="34" r="3" fill="#fff"/><path d="M10 24l3 2M26 12v4M42 24l-3 2"/></svg></div>
  <div class="service-name">LOREM IPSUM</div>
  <div class="service-text">Lorem ipsum dolor sit amet, consectetur adipiscing elit, sed do eiusmod tempor.</div>
</div>
<div class="service" style="left:587px;top:1411px">
  <div class="service-icon"><svg width="38" height="48" viewBox="0 0 38 48"><rect x="2" y="2" width="34" height="44" rx="3" fill="none" stroke="#fff" stroke-width="3"/><rect x="8" y="8" width="22" height="9" fill="#fff"/><g fill="#fff"><rect x="8" y="22" width="5" height="5"/><rect x="17" y="22" width="5" height="5"/><rect x="26" y="22" width="5" height="5"/><rect x="8" y="31" width="5" height="5"/><rect x="17" y="31" width="5" height="5"/><rect x="26" y="31" width="5" height="11"/><rect x="8" y="38" width="14" height="4"/></g></svg></div>
  <div class="service-name">LOREM IPSUM</div>
  <div class="service-text">Lorem ipsum dolor sit amet, consectetur adipiscing elit, sed do eiusmod tempor.</div>
</div>
<div class="service" style="left:851px;top:1411px">
  <div class="service-icon"><svg width="40" height="50" viewBox="0 0 40 50" fill="none" stroke="#fff" stroke-width="3"><rect x="4" y="7" width="32" height="40" rx="3"/><rect x="13" y="3" width="14" height="8" fill="#f07f06"/><path d="M10 21h3M18 21h12M10 29h3M18 29h12M10 37h3M18 37h12"/></svg></div>
  <div class="service-name">LOREM IPSUM</div>
  <div class="service-text">Lorem ipsum dolor sit amet, consectetur adipiscing elit, sed do eiusmod tempor.</div>
</div>

<span class="btn" style="left:503px;top:1612px;width:194px;height:37px">View More</span>

<h2 class="section-title" style="left:0;width:1200px;text-align:center;top:1765px">TESTIMONIAL</h2>
<span class="arrow prev" style="left:87px;top:1882px"><svg width="14" height="22" viewBox="0 0 14 22"><path d="M11 2 3 11l8 9" stroke="#fff" stroke-width="3" fill="none"/></svg></span>
<span class="arrow next" style="left:1074px;top:1882px"><svg width="14" height="22" viewBox="0 0 14 22"><path d="M3 2l8 9-8 9" stroke="#fff" stroke-width="3" fill="none"/></svg></span>
<div class="abs" style="left:178px;top:1830px;width:154px;height:154px;border-radius:50%;border:3px solid #e6e6e6;background:radial-gradient(circle at 50% 40%,#d9b59e,#8a6a5a 60%,#c9c3c7)" role="img" aria-label="Portrait of the client giving the testimonial"></div>
<div class="abs" style="left:300px;top:1830px;width:62px;height:62px;border-radius:50%;background:#fff;box-shadow:0 1px 4px rgba(0,0,0,.25);display:flex;align-items:center;justify-content:center">
  <svg width="30" height="22" viewBox="0 0 30 22" fill="#f07f06"><path d="M2 22V12C2 5 6 1 12 0v4C8 5 7 8 7 10h5v12zM18 22V12C18 5 22 1 28 0v4c-4 1-5 4-5 6h5v12z"/></svg>
</div>
<p class="quote-text">Lorem Ipsum is simply dummy text of the printing and typesetting industry. Lorem Ipsum has been the industry's standard dummy text ever since the 1500s, when an unknown printer took a galley of type and scrambled it to make a type specimen book. It has survived not only five centuries, but also the leap into electronic typesetting, remaining essentially unchanged.</p>
<div class="quote-by"><span class="rule"></span><span class="name">JANE DOE</span>&nbsp;|&nbsp;&nbsp;&nbsp; Lorem Ipsum is</div>

<section class="contact-zone"></section>
<h2 class="section-title" style="left:87px;top:2102px">OUR ADDRESS</h2>
<h2 class="section-title" style="left:551px;top:2102px">CONTACT US</h2>

<svg class="addr-icon" style="top:2166px" width="13" height="12" viewBox="0 0 13 12"><path d="M6.5 0 0 6h2v6h3.5V8h2v4H11V6h2z" fill="#555"/></svg>
<p class="addr" style="top:2163px">Lorem Ipsum is simply dummy text of the<br>printing and typesetting industry.</p>
<svg class="addr-icon" style="top:2228px" width="12" height="12" viewBox="0 0 12 12"><path d="M2 0h3l1 3-2 1.5a7 7 0 0 0 3.5 3.5L9 6l3 1v3c0 1-1 2-2 2C4.5 12 0 7.5 0 2 0 1 1 0 2 0z" fill="#555"/></svg>
<p class="addr" style="top:2224px">000 - 000 - 000<br>000 - 000 - 000</p>
<svg class="addr-icon" style="top:2286px" width="13" height="12" viewBox="0 0 13 12"><rect x="0" y="3" width="13" height="9" fill="#555"/><rect x="3" y="0" width="7" height="5" fill="#555" stroke="#fff"/><rect x="3" y="6" width="5" height="3" fill="#fff"/></svg>
<p class="addr" style="top:2282px">000 - 000 - 000<br>000 - 000 - 000</p>

<h2 class="section-title" style="left:85px;top:2352px">FOLLOW US</h2>
<span class="social" style="left:85px" aria-label="Social profile"></span>
<span class="social" style="left:139px" aria-label="Social profile"></span>
<span class="social" style="left:194px" aria-label="Social profile"></span>
<span class="social" style="left:248px" aria-label="Social profile"></span>

<div class="field" style="top:2167px;height:40px">Name</div>
<div class="field" style="top:2220px;height:40px">Email</div>
<div class="field" style="top:2273px;height:124px">Message</div>
<span class="btn" style="left:551px;top:2412px;width:195px;height:37px">Message</span>

<footer class="footer-bar">© 2018, MB- Prismo. All Rights Reserved.</footer>

</body>
</html>
```